We need a flyer (size Din A4, folded, see image).
Attached you will find the content with a rough arrangement.
The inner part will contain some Q&A, we have sketched two possible arrangements of the content.
We are looking for a professional design and a good, clean layout.
Maybe you have some ideas how to arrange the content in a smarter way, we are open for suggestions.
The draft contains no images. It would be good to have an explaining image at least on the front of the flyer.
Attached you will find some stock photos we are using on our website, but you can also propose your own images.
If useful, here is our webpage:
https://vorn-strom.de/
and the landing page for the offering
https://vorn-strom. en/charging-solutions-for-house-management-and-routes/
(this landing page is not professionally designed, so feel free to create a better design for the flyer)
Our target group are real estate managers/facility managers of larger apartment buildings.
The offering is: full-serviced solutions for charging infrastructure for electric cars at the parking lots for residents.
Please do not hesitate to contact me, if you need further information.
Target Market(s)
Professionals in real estate management, facility management
Industry/Entity Type
charging infrastructures for electric cars, focus: appartment buildings

```html
<!DOCTYPE html>
<html lang="de">
<head>
<meta charset="utf-8">
<title>vorn-strom – Faltflyer Ladeinfrastruktur</title>
<link rel="stylesheet" href="https://fonts.googleapis.com/css2?family=Open+Sans:wght@400;600;700;800&display=swap">
<style>
:root{
  --bg:#e4e4e4;
  --navy:#1b1a2c;
  --navy-2:#262440;
  --magenta:#c92f8c;
  --pink:#e04aa0;
  --purple:#7a4cc0;
  --violet:#9b5fd0;
  --white:#ffffff;
  --ink:#2d2b3f;
  --muted:#6c6a80;
  --soft:#f6eef7;
}
*{box-sizing:border-box;margin:0;padding:0}
html,body{width:1200px;height:2387px;overflow:hidden}
body{background:var(--bg);font-family:"Open Sans",Arial,sans-serif;color:var(--ink);position:relative}
.sheet{position:absolute;left:40px;width:1120px;height:792px;display:flex;box-shadow:0 12px 30px rgba(0,0,0,.18);background:var(--white)}
.sheet--outer{top:268px}
.sheet--inner{top:1328px}
.panel{position:relative;width:373.33px;height:100%;overflow:hidden}
.panel+.panel{border-left:1px solid rgba(0,0,0,.06)}
.photo{position:absolute;left:0;right:0}
.curve{position:absolute;left:0;width:100%}
.pill{display:inline-block;border-radius:30px;background:linear-gradient(90deg,var(--purple),var(--magenta));color:var(--white);font-weight:700;font-size:15px;padding:9px 26px;letter-spacing:.3px}
.brand{display:flex;align-items:center;gap:10px;font-weight:800;color:var(--navy);font-size:30px}
.brand__dot{width:22px;height:22px;border-radius:50%;background:var(--magenta)}

/* front */
.front{background:var(--navy)}
.front__head{position:absolute;top:0;left:0;right:0;height:190px;display:flex;justify-content:center;padding-top:62px}
.front__photo{top:150px;height:380px;background:radial-gradient(circle at 30% 70%,#6d6f9a 0,transparent 35%),linear-gradient(135deg,#3c3d5e,#5a5d86 45%,#232238 100%)}
.front__text{position:absolute;left:30px;right:30px;top:560px;text-align:center;color:var(--white)}
.front__title{font-size:20px;font-weight:700;line-height:1.35}
.front__sub{font-size:17px;line-height:1.4;margin-top:10px}
.front__cta{margin-top:26px}

/* back */
.back{background:linear-gradient(180deg,var(--purple) 0,var(--violet) 35%,var(--magenta) 70%)}
.back__head{position:absolute;top:0;left:0;right:0;height:130px;display:flex;justify-content:center;padding-top:44px}
.back__head .brand{font-size:24px}
.features{position:absolute;top:160px;left:30px;right:30px;list-style:none}
.feature{display:flex;gap:12px;color:var(--white);font-size:12px;line-height:1.45;margin-bottom:16px}
.icon-box{flex:0 0 34px;height:34px;border:2px solid var(--white);border-radius:6px;display:flex;align-items:center;justify-content:center}
.back__contact{position:absolute;top:370px;left:0;right:0;text-align:center;color:var(--white)}
.back__contact h3{font-size:18px;font-weight:700;line-height:1.3}
.back__contact .url{display:inline-block;margin-top:12px;background:var(--navy);color:var(--white);border-radius:24px;padding:7px 22px;font-weight:700;font-size:15px}
.back__contact .phone{margin-top:10px;font-size:16px}
.back__foot{position:absolute;bottom:0;left:0;right:0;height:250px;background:var(--navy);color:#cfcde0;font-size:12px;line-height:1.55;padding:60px 30px 0 70px}
.back__foot p+p{margin-top:12px}

/* flap */
.flap__photo{top:0;height:230px;background:linear-gradient(120deg,#8c3f84,#b14f9d 40%,#c9cd88 100%)}
.flap__body{position:absolute;top:250px;left:30px;right:28px}
.flap__lead{font-size:15px;line-height:1.45;color:var(--ink)}
.flap__lead ul{list-style:none;margin-top:6px;padding-left:18px}
.flap__lead li::before{content:"✓ ";color:var(--magenta);font-weight:700}
.bullets{list-style:none;margin-top:18px}
.bullet{display:flex;gap:10px;font-size:11.5px;line-height:1.45;color:var(--muted);margin-bottom:12px}
.bullet .icon-box{flex:0 0 26px;height:26px;border-color:var(--magenta)}
.flap__foot{position:absolute;bottom:0;left:0;right:0;height:96px;background:var(--navy);display:flex;align-items:center;justify-content:center}

/* inside */
.inside__photo{position:absolute;top:0;left:0;width:746.66px;height:250px;background:linear-gradient(100deg,#b9598f 0,#6e5a8c 35%,#3e4b63 65%,#7f9aa6 100%)}
.qa{padding:270px 24px 0}
.section-tag{display:inline-block;background:linear-gradient(90deg,var(--magenta),var(--purple));color:var(--white);font-weight:700;font-size:15px;padding:6px 18px;border-radius:0 20px 20px 0;margin-left:-24px}
.qa__list{list-style:none;margin-top:16px}
.qa__item{position:relative;border:1.5px solid var(--pink);border-radius:12px;padding:8px 54px 8px 12px;font-size:11.5px;line-height:1.35;color:var(--magenta);margin-bottom:10px;min-height:62px;display:flex;align-items:center}
.qa__item::after{content:"?";position:absolute;right:10px;top:50%;transform:translateY(-50%);width:34px;height:34px;border-radius:50%;background:linear-gradient(135deg,var(--magenta),var(--purple));color:var(--white);font-weight:800;display:flex;align-items:center;justify-content:center}
.solution{padding:270px 26px 0}
.solution h2{font-size:17px;font-weight:700;color:var(--navy)}
.solution p{font-size:11.5px;line-height:1.6;color:var(--muted);margin-top:14px}
.solution strong{color:var(--ink)}
.steps{background:var(--navy);color:var(--white)}
.steps h2{position:absolute;top:40px;left:30px;right:30px;font-size:18px;line-height:1.3;color:var(--pink);font-weight:700}
.step-list{position:absolute;top:130px;left:30px;right:24px;list-style:none}
.step{display:flex;gap:12px;margin-bottom:18px}
.step .icon-box{flex:0 0 36px;height:36px;border:none;background:linear-gradient(135deg,var(--magenta),var(--purple))}
.step h4{font-size:14px;color:var(--pink);font-weight:700}
.step p{font-size:11px;line-height:1.45;color:#d5d3e4}
.steps__cta{position:absolute;top:490px;left:0;right:0;text-align:center}
.steps__photo{top:560px;height:232px;background:linear-gradient(135deg,#cfe1ee,#8fb1cc 50%,#e86a6a 100%)}
</style>
</head>
<body>

<!-- Outer side -->
<section class="sheet sheet--outer">
  <!-- inside flap -->
  <article class="panel flap">
    <div class="photo flap__photo" role="img" aria-label="Foto: Ladestecker steckt in einem Elektroauto"></div>
    <svg class="curve" style="top:190px" viewBox="0 0 373 60" height="60" preserveAspectRatio="none"><path d="M0 40 Q190 0 373 20 L373 60 L0 60Z" fill="#fff"/><path d="M0 40 Q190 0 373 20" stroke="#c92f8c" stroke-width="3" fill="none"/></svg>
    <div class="flap__body">
      <div class="flap__lead">Bieten Sie Ihren Bewohnern Lademöglichkeiten für ihre Elektrofahrzeuge –
        <ul><li>einfach,</li><li>unkompliziert und</li><li>zukunftsfähig</li></ul>
      </div>
      <ul class="bullets">
        <li class="bullet"><span class="icon-box"></span>Zukunftsfähig durch flexible Abrechnung, passend für verschiedene Einsatzmöglichkeiten</li>
        <li class="bullet"><span class="icon-box"></span>Leichter, schneller Einstieg in das Thema, unkompliziert und professionell betreut</li>
        <li class="bullet"><span class="icon-box"></span>Aufbau und Betrieb von Ladelösungen kosteneffizient für Verwaltung und WEG</li>
      </ul>
    </div>
    <div class="flap__foot"><span class="pill">www.vorn-strom.de</span></div>
  </article>

  <!-- back -->
  <article class="panel back">
    <svg class="curve" style="top:0" viewBox="0 0 373 140" height="140" preserveAspectRatio="none"><path d="M0 0 H373 V100 Q190 150 0 115Z" fill="#fff"/></svg>
    <div class="back__head"><div class="brand"><span class="brand__dot"></span>vorn-strom.de</div></div>
    <ul class="features">
      <li class="feature"><span class="icon-box"></span>Hausverwaltungen werden von Planung und Aufwand entlastet, der Betrieb läuft komplett über uns</li>
      <li class="feature"><span class="icon-box"></span>Sichere Umsetzung nach neuem Gebäude-Elektromobilitätsgesetz für alle Stellplätze der Anlage</li>
      <li class="feature"><span class="icon-box"></span>Als Betreiber tragen wir die Verantwortung für Wartung, Abrechnung und Service gegenüber Nutzern</li>
    </ul>
    <div class="back__contact">
      <h3>Jetzt Beratungsgespräch<br>anfordern unter:</h3>
      <span class="url">www.vorn-strom.de/WEG</span>
      <p class="phone">oder ☎ 08031 / 482 19 60</p>
    </div>
    <svg class="curve" style="bottom:240px" viewBox="0 0 373 40" height="40" preserveAspectRatio="none"><path d="M0 40 Q190 -10 373 25 L373 40Z" fill="#1b1a2c"/></svg>
    <div class="back__foot">
      <p>vorn-strom GmbH<br>Lindenweg 12<br>83022 Rosenheim</p>
      <p>HRB 518204<br>Amtsgericht Traunstein<br>Geschäftsführung: Jana Berger</p>
      <p>Email: info@vorn-strom.de<br>Tel.: 08031 / 482 19 60</p>
    </div>
  </article>

  <!-- front -->
  <article class="panel front">
    <div class="photo front__photo" role="img" aria-label="Foto: Ladesäule mit eingestecktem Ladekabel"></div>
    <svg class="curve" style="top:0" viewBox="0 0 373 200" height="200" preserveAspectRatio="none"><path d="M0 0 H373 V150 Q190 215 0 170Z" fill="#fff"/><path d="M373 150 Q190 215 0 170" stroke="#c92f8c" stroke-width="3" fill="none"/></svg>
    <div class="front__head"><div class="brand"><span class="brand__dot"></span>vorn-strom.de</div></div>
    <svg class="curve" style="top:490px" viewBox="0 0 373 60" height="60" preserveAspectRatio="none"><path d="M0 20 Q190 70 373 30 L373 60 L0 60Z" fill="#1b1a2c"/><path d="M0 20 Q190 70 373 30" stroke="#c92f8c" stroke-width="3" fill="none"/></svg>
    <div class="front__text">
      <h1 class="front__title">Flexible Ladeinfrastrukturen<br>für die Elektromobilität</h1>
      <p class="front__sub">für Mieter und Eigentümer<br>einfach, unkompliziert und zukunftsfähig</p>
      <div class="front__cta"><span class="pill">www.vorn-strom.de</span></div>
    </div>
  </article>
</section>

<!-- Inner side -->
<section class="sheet sheet--inner">
  <div class="inside__photo" role="img" aria-label="Foto: Elektroautos an Ladestationen in einer Tiefgarage"></div>
  <svg class="curve" style="top:200px;width:746.66px;z-index:1" viewBox="0 0 746 60" height="60" preserveAspectRatio="none"><path d="M0 30 Q370 -10 746 40 L746 60 L0 60Z" fill="#fff"/><path d="M0 30 Q370 -10 746 40" stroke="#c92f8c" stroke-width="3" fill="none"/></svg>

  <article class="panel qa">
    <span class="section-tag">Problem / Fragestellung</span>
    <ul class="qa__list">
      <li class="qa__item">Ein Bewohner will eine Wallbox – was nun?</li>
      <li class="qa__item">Der Stromanschluss reicht nicht, wenn alle Bewohner eine Wallbox wollen?</li>
      <li class="qa__item">Sind die Voraussetzungen für Ladeinfrastruktur in der WEG bereits gegeben?</li>
      <li class="qa__item">Die Bewohner haben keine fest zugewiesenen Stellplätze?</li>
      <li class="qa__item">Wer kann helfen, eine professionelle und zukunftsfähige Lösung zu entwickeln?</li>
      <li class="qa__item">Bei uns wurden bereits Wallboxen montiert. Was ist zu tun?</li>
    </ul>
  </article>

  <article class="panel solution">
    <h2>Der Lösungsansatz von vorn-strom</h2>
    <p>Unser Ansatz beginnt mit einer Analyse Ihrer Anlage. Wir prüfen den Netzanschluss, die Stellplätze und die Wünsche der Bewohner und zeigen Ihnen realistische Wege auf.</p>
    <p>Daraus entwickeln wir ein Konzept, das sich Schritt für Schritt erweitern lässt. So profitieren heutige Nutzer sofort, und spätere Nutzer können jederzeit hinzukommen.</p>
    <p>Mit intelligentem Lastmanagement verteilen wir die verfügbare Leistung auf alle Ladepunkte, ohne den Hausanschluss teuer ausbauen zu müssen.</p>
    <p><strong>vorn-strom</strong> übernimmt als Betreiber die technische Umsetzung, den laufenden Service und die Abrechnung direkt mit den Nutzern – die Verwaltung wird spürbar entlastet.</p>
    <p>Bestehende Wallboxen anderer Hersteller binden wir nach Prüfung in die Lösung ein.</p>
  </article>

  <article class="panel steps">
    <h2>Die Schritte zur Ladeinfrastruktur in Ihrer Anlage</h2>
    <ul class="step-list">
      <li class="step"><span class="icon-box"></span><div><h4>Erstprüfung</h4><p>Bestandsaufnahme vor Ort<br>Ermittlung der Leistungsreserve</p></div></li>
      <li class="step"><span class="icon-box"></span><div><h4>Konzeption</h4><p>Planung der Anlage<br>Angebot und Beschlussvorlage</p></div></li>
      <li class="step"><span class="icon-box"></span><div><h4>Installation</h4><p>Montage der Ladepunkte<br>Inbetriebnahme und Übergabe</p></div></li>
      <li class="step"><span class="icon-box"></span><div><h4>Betrieb</h4><p>Service und Wartung<br>Abrechnung mit den Nutzern</p></div></li>
    </ul>
    <div class="steps__cta"><span class="pill">www.vorn-strom.de</span></div>
    <div class="photo steps__photo" role="img" aria-label="Foto: Ladekabel am Elektroauto mit leuchtender Ladebuchse"></div>
    <svg class="curve" style="top:550px" viewBox="0 0 373 50" height="50" preserveAspectRatio="none"><path d="M0 0 H373 V10 Q190 60 0 30Z" fill="#1b1a2c"/><path d="M373 10 Q190 60 0 30" stroke="#c92f8c" stroke-width="3" fill="none"/></svg>
  </article>
</section>

</body>
</html>
```